Leadership Training Business Needs a business card design

We need a business card designed for our company based in Auckland, New Zealand called Crestfield Guidance Services. We conduct a variety of residential programmes that provide for differnet management levels. These programmes are designed to familiarise managers with important leadership concepts and techniques. This learning is reinforced through the provision of real workplace feedback and the use of action learning opportunities (experiential exercises) to develop the participants' leadership skills and potential. We would like to add our tag line which is:
Inspires Direction - Instils Values - Delivers Results
We would like the card to be a white background but would consider a different background colour on the back. Possibly include the following words on the back:
- Organisational Development
- Positive Cultural Change
- Leadership Programmes
- Practical Development "Tools"
- Crew Balance Inventory
- 360o degree Assessments
- Strengths Based Training
- Coaching and Mentoring

Industry/Entity Type

Business

Requirements
Must have
• Company Name, logo, contact details, website address and email.
• Persons name and their title

```html
<!DOCTYPE html>
<html lang="en">
<head>
<meta charset="utf-8">
<title>Crestfield Guidance Services – Business Card</title>
<link rel="stylesheet" href="https://fonts.googleapis.com/css2?family=Open+Sans:ital,wght@0,400;0,700;1,400&display=swap">
<style>
  :root {
    --bg: #ececec;
    --card: #ffffff;
    --blue: #0a8fd6;
    --blue-deep: #0b62b0;
    --blue-text: #1a6fbb;
    --ink: #1d1d1d;
    --ink-soft: #4a4a4a;
  }
  * { margin: 0; padding: 0; box-sizing: border-box; }
  html, body {
    width: 1200px; height: 1200px; overflow: hidden;
    background: var(--bg);
    font-family: "Open Sans", sans-serif;
  }
  .card {
    position: absolute;
    left: 175px;
    width: 850px; height: 483px;
    background: var(--card);
    overflow: hidden;
  }
  .card--front { top: 75px; }
  .card--back  { top: 642px; }
  .card__art {
    position: absolute; inset: 0;
    width: 100%; height: 100%;
  }
  .line {
    position: absolute;
    left: 0; right: 0;
    text-align: center;
    white-space: nowrap;
    line-height: 1;
  }
  .front__company  { top: 176px; font-size: 25px; color: var(--ink); }
  .front__division { top: 202px; font-size: 24px; color: var(--blue-text); }
  .front__name     { top: 274px; font-size: 26px; color: var(--ink-soft); }
  .front__title    { top: 308px; font-size: 20px; font-style: italic; color: var(--ink-soft); }
  .front__tagline  {
    top: 428px; font-size: 25px; font-weight: 700;
    color: #fff; letter-spacing: 0.6px;
  }
  .back__brand {
    position: absolute;
    left: 41px; width: 240px;
    text-align: center;
    color: #fff;
    font-size: 18px;
    line-height: 1.15;
    top: 410px;
  }
  .back__services {
    position: absolute;
    left: 442px; top: 172px;
    list-style: none;
  }
  .back__services li {
    font-size: 19px;
    font-weight: 700;
    color: var(--blue-text);
    letter-spacing: 0.6px;
    line-height: 36.7px;
    white-space: nowrap;
  }
</style>
</head>
<body>

<section class="card card--front" aria-label="Business card front">
  <svg class="card__art" viewBox="0 0 707 402" preserveAspectRatio="none" aria-hidden="true">
    <path d="M0,353 Q353,262 707,353 L707,365 Q353,270 0,365 Z" fill="var(--blue-deep)"/>
    <path d="M0,372 Q353,290 707,372 L707,402 L0,402 Z" fill="var(--blue)"/>
  </svg>
  <p class="line front__company">Crestfield Guidance Services</p>
  <p class="line front__division">Leadership Programmes</p>
  <p class="line front__name">Daniel Ashworth</p>
  <p class="line front__title">Facilitator</p>
  <p class="line front__tagline">Inspires Direction | Instils Values | Delivers Results</p>
</section>

<section class="card card--back" aria-label="Business card back">
  <svg class="card__art" viewBox="0 0 707 402" preserveAspectRatio="none" aria-hidden="true">
    <rect width="707" height="402" fill="var(--blue)"/>
    <path d="M40,0 L544,0 C640,60 700,180 690,260 C682,330 640,380 604,402 L364,402 C345,330 330,240 334,175 C290,145 220,118 150,125 C90,130 40,145 0,160 L0,30 Z" fill="var(--card)"/>
    <path d="M544,0 C640,60 700,180 690,260 C682,330 640,380 604,402" fill="none" stroke="var(--blue-deep)" stroke-width="5"/>
    <path d="M334,175 C290,145 220,118 150,125 C90,130 40,145 0,160" fill="none" stroke="var(--blue-deep)" stroke-width="3"/>
  </svg>
  <div class="back__brand">
    <p>Crestfield Guidance Services</p>
    <p>Leadership Programmes</p>
  </div>
  <ul class="back__services">
    <li>Organisational Development</li>
    <li>Positive Cultural Change</li>
    <li>Leadership Programmes</li>
    <li>Practical Development "Tools"</li>
    <li>Crew Balance Inventory</li>
    <li>360° degree Assessments</li>
    <li>Strengths Based Training</li>
    <li>Coaching and Mentoring</li>
  </ul>
</section>

</body>
</html>
```